BrightFern Web Design Project

BrightFern IT solutions, a IT mananaged services company is looking to redesign current website (brightfernsolutions.example).

The website should convey professionalism within the managed it services community. The layout should invite users to explore other areas of the site. Should contain tools and other current information that clients or potential clients would find useful. Product pages, special offers and informational pages should be easily editable by non-programmers. Tidewarden.example is a good site to review as an example of the design components we like.

Target Market(s)

Professional services companies with 10-100 users

Industry/Entity Type

It Company

Requirements
Must have
• • Clickable icons and graphics are good
• SEO - Wordpress could be a great platform for us to work from as we already have internal experience with it and it’s easy to update. If not Wordpress, we would need something that is easy to SEO optimize
• An “our team” section with pictures
• Sell the message to potential clients why they need managed services
• Home page needs to convey our core services at a glance
• Home page needs to load quickly
• Screenshots of our monitoring and security reports
• Easy for us to update/edit certain areas
o New products
o Testimonials
Nice to have
• • Something like TW’s savings calculator - http://www.tidewarden.example/it-savings-calculator/
• Webform to enter service ticket requests
• Motion of home page banner
• Maybe pull in RSS feeds from current tech news sources
• Rotating content on all pages to keep it fresh
• “Fern-up” feature for monthly promos
Should not have
• • Should not be overly "techie" in feel.
• Not overly wordy (like current site)

```html
<!DOCTYPE html>
<html lang="en">
<head>
<meta charset="utf-8">
<title>BrightFern IT Solutions</title>
<link href="https://fonts.googleapis.com/css2?family=Arimo:wght@400;700&family=Bebas+Neue&display=swap" rel="stylesheet">
<style>
:root{
  --green:#6cc02c;
  --green-dark:#4e9e16;
  --green-light:#8fd44a;
  --text:#333;
  --muted:#777;
  --soft:#999;
  --hero-bg:#f7e9ec;
  --footer:#2e2e2e;
  --footer-text:#aaa;
  --white:#fff;
  --line:#dcdcdc;
}
*{box-sizing:border-box;margin:0;padding:0}
html,body{width:971px;height:1200px;overflow:hidden;background:var(--white);font-family:"Arimo",Arial,sans-serif;color:var(--text)}
.page{position:relative;width:971px;height:1200px}
.abs{position:absolute}

.brand{left:112px;top:28px;width:110px;text-align:center}
.brand-dot{width:52px;height:52px;border-radius:50%;background:var(--green);margin:0 auto 6px}
.brand-name{font-size:19px;font-weight:700;color:var(--green-dark);display:block}
.brand-sub{font-size:9px;font-weight:700;color:var(--green-dark);letter-spacing:.5px}

.contact{left:722px;top:15px;font-size:10px;line-height:15px;color:#333}
.contact svg{position:absolute;left:0;top:2px}
.contact p{padding-left:21px}

.nav{left:229px;top:57px;width:642px;height:28px;background:linear-gradient(#8fd44a,#5fb21f);border-radius:3px 3px 0 0;display:flex;align-items:flex-end}
.nav a{color:var(--white);font-size:12px;text-decoration:none;padding:0 19px;line-height:26px;border-right:1px solid rgba(255,255,255,.25)}
.nav a.active{background:var(--white);color:#333;border-radius:3px 3px 0 0;height:25px;line-height:24px;border:none}
.nav .support{margin-left:auto;border:none}
.subnav{left:229px;top:85px;width:642px;height:29px;background:var(--white);box-shadow:0 2px 3px rgba(0,0,0,.15);font-size:10px;color:#333;display:flex;align-items:center;padding-left:12px;gap:0}
.subnav span{white-space:nowrap}
.subnav .sep{padding:0 14px}

.hero{left:101px;top:126px;width:770px;height:273px;background:radial-gradient(circle at 70% 40%,#fff 0%,var(--hero-bg) 70%)}
.hero-kicker{left:160px;top:180px;font-family:"Bebas Neue",sans-serif;font-size:24px;color:#333;letter-spacing:.3px}
.hero-title{left:160px;top:200px;font-family:"Bebas Neue",sans-serif;font-size:38px;color:var(--green);letter-spacing:.3px}
.hero-copy{left:160px;top:252px;font-size:13px;line-height:20px;color:#444}
.hero-btn{left:160px;top:305px;width:220px;height:47px;background:linear-gradient(#8fd44a,#5fb21f);border-radius:3px;color:var(--white);font-family:"Bebas Neue",sans-serif;font-size:22px;display:flex;align-items:center;justify-content:center}
.dots{left:162px;top:370px;display:flex;gap:8px}
.dots i{width:13px;height:13px;border-radius:50%;background:#666;display:block}
.dots i.on{background:var(--white);border:2px solid #666}
.screen{left:500px;top:155px;width:322px;height:262px;background:linear-gradient(#f4f4f4,#cfcfcf);border-radius:6px}

.features{left:101px;top:413px;width:770px;height:143px;background:linear-gradient(#7ccb36,#55ad1a);display:flex}
.feature{flex:1;position:relative;padding:12px 10px 0 24px;color:var(--white)}
.feature + .feature{border-left:1px solid rgba(255,255,255,.35)}
.feature-icon{position:absolute;left:6px;top:10px;width:20px;height:20px;border-radius:50%;background:rgba(255,255,255,.85)}
.feature h3{font-size:12.5px;font-weight:700;line-height:15px;padding-left:8px;min-height:32px}
.feature p{font-size:10px;line-height:14px;padding-left:0;margin-top:0;color:#f4ffe9}
.feature .more{position:absolute;right:14px;bottom:7px;font-size:10px}

.intro{left:101px;top:571px;width:545px}
.intro h2{font-size:13px;font-weight:400;line-height:20px;color:var(--green-dark);margin-bottom:14px}
.intro p{font-size:9.5px;line-height:14px;color:var(--muted);text-align:justify;margin-bottom:12px}

.team{left:668px;top:570px;width:205px;height:75px;background:linear-gradient(#7ccb36,#55ad1a)}
.team h3{font-family:"Bebas Neue",sans-serif;font-size:21px;color:var(--white);text-align:center;padding-top:4px;font-weight:400}
.team-photo{position:absolute;left:40px;top:28px;width:125px;height:47px;background:linear-gradient(#6a6a6a,#3c3c3c)}
.testimonial{left:668px;top:652px;width:205px;height:121px;border:1px solid var(--line);border-radius:3px;background:linear-gradient(#fff,#eee);padding:8px 12px}
.testimonial h4{font-size:13px;font-weight:400;color:#333;margin-bottom:10px}
.testimonial h4 b{color:var(--green);font-size:18px;margin-right:6px}
.testimonial p{font-size:9.5px;line-height:13px;color:var(--soft)}
.testimonial .who{text-align:right;font-size:11px;color:#555;margin-top:4px}
.testimonial .who small{display:block;font-size:9px;color:var(--soft)}

.rule{left:101px;top:782px;width:770px;height:1px;background:var(--line)}

.shot-main{left:103px;top:796px;width:234px;height:152px;background:linear-gradient(#f0f0f0,#fafafa);border:1px solid var(--line);border-radius:4px 4px 0 0}
.product{left:362px;top:796px}
.product h3{font-size:12.5px;font-weight:400;color:var(--green-dark);line-height:20px}
.product ul{list-style:none;margin-top:8px}
.product li{font-size:10.5px;color:#444;height:26px;display:flex;align-items:center}
.product li svg{margin-right:10px}
.thumb{width:121px;height:69px;border:1px solid var(--line);background:linear-gradient(#f5f5f5,#fdfdfd)}

.footer{left:0;top:986px;width:971px;height:214px;background:var(--footer)}
.fcol h4{font-size:12px;font-weight:700;color:var(--white);margin-bottom:12px}
.fcol li{list-style:none;font-size:9.5px;color:var(--footer-text);line-height:16.7px}
.press h5,.blog h5{font-size:9.5px;font-weight:700;color:#ddd;margin-bottom:3px}
.press p{font-size:9.5px;color:#888;line-height:12.5px;margin-bottom:10px;width:186px}
.post{display:flex;gap:10px;margin-bottom:12px}
.post .date{width:24px;text-align:center;color:#666;font-size:9px;font-weight:700}
.post .date b{display:block;font-size:19px;line-height:20px}
.post p{font-size:9.5px;color:#888;line-height:12.5px;width:220px}
.visit{left:777px;top:1168px;font-size:10px;color:var(--footer-text)}
</style>
</head>
<body>
<div class="page">

  <div class="abs brand">
    <div class="brand-dot"></div>
    <span class="brand-name">BrightFern</span>
    <span class="brand-sub">IT SOLUTIONS</span>
  </div>

  <div class="abs contact">
    <svg width="12" height="26" viewBox="0 0 12 26"><path d="M4 1h4v6H5v12h3v6H4C1 25 0 20 0 13S1 1 4 1z" fill="#6cc02c"/></svg>
    <p>Toll Free: (888) 555-0142</p>
    <p>Phone: (480) 555-0187</p>
  </div>

  <nav class="abs nav">
    <a>Home</a><a class="active">Solutions</a><a>Products</a><a>About Us</a><a>Contact</a><a class="support">Remote Support</a>
  </nav>
  <div class="abs subnav">
    <span>Network Design &amp; Consulting</span><span class="sep">|</span>
    <span>On-Site Retainer Service</span><span class="sep">|</span>
    <span>Remote Retainer</span><span class="sep">|</span>
    <span>Remote Management</span><span class="sep">|</span>
    <span>Network Mapping</span>
  </div>

  <section class="abs hero"></section>
  <div class="abs hero-kicker">Every company needs to</div>
  <div class="abs hero-title">Grow to survive.</div>
  <p class="abs hero-copy">We make sure your technology is ready<br>for that growth when you are.</p>
  <div class="abs hero-btn">Read more about us</div>
  <div class="abs dots"><i></i><i></i><i></i><i class="on"></i><i></i></div>
  <div class="abs screen" role="img" aria-label="Desktop monitor showing monitoring and security reports chart"></div>

  <section class="abs features">
    <div class="feature"><span class="feature-icon"></span><h3>IT Consulting Services</h3><p>Insure that your existing system receives quality service. Bright-Fern will troubleshoot problems, install new software or parts, and keep your system in optimal con-dition...</p><span class="more">Read more..</span></div>
    <div class="feature"><span class="feature-icon"></span><h3>IT Service Programs</h3><p>Insure that your existing system receives quality service. Bright-Fern will troubleshoot problems, install new software or parts, and keep your system in optimal con-dition...</p><span class="more">Read more..</span></div>
    <div class="feature"><span class="feature-icon"></span><h3>Security Vulnerability Scan</h3><p>Insure that your existing system receives quality service. Bright-Fern will troubleshoot problems, install new software or parts, and keep your system in optimal con-dition...</p><span class="more">Read more..</span></div>
    <div class="feature"><span class="feature-icon"></span><h3>Data Backup and Recovery</h3><p>Insure that your existing system receives quality service. Bright-Fern will troubleshoot problems, install new software or parts, and keep your system in optimal con-dition...</p><span class="more">Read more..</span></div>
  </section>

  <article class="abs intro">
    <h2>BrightFern can help your business harness the power of new technology,<br>making your business fast and efficient.</h2>
    <p>In the information age of today, one must stay abreast of current technology in order to thrive. New advancements are made daily in dispersing information and collaborative computing. High-speed networks aid in the exchange of electronic information between businesses, their customers, vendors, and peers. Businesses that are quick to act and effectively implement this technology will rise to the top.</p>
    <p>Lorem Ipsum is simply dummy text of the printing and typesetting industry. Lorem Ipsum has been the industry's standard dummy text ever since the 1500s, when an unknown printer took a galley of type and scrambled it to make a type specimen book. It has survived not only five centuries, but also the leap into electronic typesetting, remaining essentially unchanged. It was popularised in the 1960s with the release of Typeline sheets containing Lorem Ipsum passages, and more recently with desktop publishing software like Pageform Studio including versions of Lorem Ipsum.</p>
  </article>

  <aside class="abs team">
    <h3>The Team</h3>
    <div class="team-photo" role="img" aria-label="Group photo of the BrightFern team"></div>
  </aside>
  <aside class="abs testimonial">
    <h4><b>“</b>Testimonials</h4>
    <p>In the information age of today, one must stay abreast of current technology in order to thrive. New advancements are made daily in dispersing information</p>
    <div class="who">Mr: Name<small>Information</small></div>
  </aside>

  <div class="abs rule"></div>

  <div class="abs shot-main" role="img" aria-label="Screenshot of the new product application window"></div>
  <div class="abs product">
    <h3>New product<br>making your business fast and efficient.</h3>
    <ul>
      <li><svg width="13" height="11" viewBox="0 0 13 11"><path d="M1 6l4 4 7-9" stroke="#6cc02c" stroke-width="2.5" fill="none"/></svg>Lorem Ipsum is simply</li>
      <li><svg width="13" height="11" viewBox="0 0 13 11"><path d="M1 6l4 4 7-9" stroke="#6cc02c" stroke-width="2.5" fill="none"/></svg>Typesetting industry.</li>
      <li><svg width="13" height="11" viewBox="0 0 13 11"><path d="M1 6l4 4 7-9" stroke="#6cc02c" stroke-width="2.5" fill="none"/></svg>Lorem Ipsum has been</li>
      <li><svg width="13" height="11" viewBox="0 0 13 11"><path d="M1 6l4 4 7-9" stroke="#6cc02c" stroke-width="2.5" fill="none"/></svg>The industry's standard</li>
    </ul>
  </div>
  <div class="abs thumb" style="left:608px;top:801px" role="img" aria-label="Product screenshot"></div>
  <div class="abs thumb" style="left:753px;top:801px" role="img" aria-label="Product screenshot"></div>
  <div class="abs thumb" style="left:608px;top:883px" role="img" aria-label="Product screenshot"></div>
  <div class="abs thumb" style="left:753px;top:883px" role="img" aria-label="Product screenshot"></div>

  <footer class="abs footer"></footer>
  <div class="abs fcol" style="left:97px;top:1020px">
    <h4>About Us</h4>
    <ul><li>About us</li><li>Jobs</li><li>Customer Stories</li><li>Press Resources</li><li>Press Releases</li><li>About us</li><li>Customer Stories</li></ul>
  </div>
  <div class="abs fcol" style="left:234px;top:1020px">
    <h4>Products</h4>
    <ul><li>CMS Platform</li><li>Mobile Applications</li><li>Tablet Apps</li><li>Seeker Toolkit</li><li>CMS Platform</li><li>Mobile Applications</li><li>Seeker Toolkit</li></ul>
  </div>
  <div class="abs fcol press" style="left:345px;top:1020px">
    <h4>Press Room</h4>
    <h5>December 01</h5><p>Lorem Ipsum is simply dummy text of the printing and typesetting industry. Lorem</p>
    <h5>December 02</h5><p>Lorem Ipsum is simply dummy text of the printing and typesetting industry. Lorem</p>
    <h5>December 03</h5><p>Lorem Ipsum is simply dummy text of the</p>
  </div>
  <div class="abs fcol blog" style="left:557px;top:1020px">
    <h4>Blog Updates</h4>
    <h5>Printing and typesetting industry</h5>
    <div class="post"><div class="date"><b>02</b>DEC</div><p>An unknown printer took a galley of type and scbled it to make a type Lorem Ipsum is simply dummy text An unknown printer took</p></div>
    <h5>Printing and typesetting industry</h5>
    <div class="post"><div class="date"><b>03</b>DEC</div><p>An unknown printer took a galley of type ascmbled it to make a type Lorem Ipsum is siply dummy text of the printing and typesetting industry.</p></div>
  </div>
  <div class="abs visit">Visit Blog</div>

</div>
</body>
</html>
```